IT services company needs a business card designed

-2 sided business card.-Front is going to be the logo raised (3D floating effect) on a black background. Make the logos spider web shiny silver and keep the spider the same design. -Back needs to have the following information:Darrel Sotho, Managing Partner, Cell: 738-402-1954, Website: Plankhorn.com, Email: Darrel@Plankhorn.com
Target Market(s)
IT Services
Industry/Entity Type
It Company
Contact Information for Business Card
-2 sided business card.
-Front is going to be the logo raised (3D floating effect) on a black background. Make the logos spider web shiny silver and keep the spider the same design.
-Back needs to have the following information:
Darrel Sotho, Managing Partner, Cell: 738-402-1954, Website: Plankhorn.com, Email: Darrel@Plankhorn.com

```html
<!DOCTYPE html>
<html lang="en">
<head>
<meta charset="utf-8">
<title>Plankhorn Business Card</title>
<link href="https://fonts.googleapis.com/css2?family=Work+Sans:wght@400;500&display=swap" rel="stylesheet">
<style>
  :root {
    --backdrop: #1b1b1c;
    --card: #0e0e0f;
    --card-edge: #232325;
    --silver: #d9d9dc;
    --contact: #c8c8cb;
    --gloss: #2c2c2f;
    --gloss-light: #3a3a3d;
  }
  * { margin: 0; padding: 0; box-sizing: border-box; }
  html, body {
    width: 1200px; height: 900px; overflow: hidden;
    background: var(--backdrop);
    font-family: "Work Sans", Arial, sans-serif;
  }
  .canvas {
    position: relative; width: 1200px; height: 900px;
    display: flex; flex-direction: column; align-items: center; justify-content: center; gap: 30px;
  }
  .card {
    position: relative; width: 700px; height: 400px;
    background: linear-gradient(135deg, #111112 0%, var(--card) 60%, #151516 100%);
    border: 1px solid var(--card-edge);
    box-shadow: 0 18px 40px rgba(0,0,0,0.55);
  }
  /* Front */
  .card-front { display: flex; align-items: center; justify-content: center; }
  .brand-name {
    font-size: 52px; font-weight: 500; letter-spacing: 2px;
    color: var(--silver);
  }
  /* Back */
  .identity {
    position: absolute; right: 420px; top: 130px; text-align: right;
  }
  .person-name {
    font-size: 31px; font-weight: 500; letter-spacing: 2px;
    color: var(--gloss-light); text-transform: uppercase;
  }
  .person-title {
    font-size: 17px; font-weight: 400; letter-spacing: 1px;
    color: var(--gloss); margin-top: 2px;
  }
  .divider {
    position: absolute; left: 300px; top: 128px; width: 1px; height: 78px;
    background: var(--gloss-light);
  }
  .contact-list {
    position: absolute; left: 322px; top: 134px; list-style: none;
  }
  .contact-item {
    display: flex; align-items: center; gap: 8px;
    font-size: 18px; letter-spacing: 1px; color: var(--contact); line-height: 24px;
  }
  .contact-icon { width: 12px; height: 12px; flex: none; }
  .address {
    position: absolute; left: 70px; bottom: 62px;
    font-size: 18px; font-weight: 500; letter-spacing: 1px; color: var(--gloss-light);
  }
</style>
</head>
<body>
  <main class="canvas">
    <section class="card card-front">
      <span class="brand-name">PLANKHORN</span>
    </section>

    <section class="card card-back">
      <div class="identity">
        <p class="person-name">Darrel Sotho</p>
        <p class="person-title">Managing Partner</p>
      </div>
      <div class="divider"></div>
      <ul class="contact-list">
        <li class="contact-item">
          <svg class="contact-icon" viewBox="0 0 12 12" fill="none" stroke="#c8c8cb" stroke-width="1.3"><path d="M2.5 1.5 L4.5 1.5 L5.2 3.8 L4 4.8 Q5 7 7.2 8 L8.2 6.8 L10.5 7.5 L10.5 9.5 Q10 10.5 9 10.5 Q2 10 1.5 3 Q1.5 2 2.5 1.5 Z"/></svg>
          738-402-1954
        </li>
        <li class="contact-item">
          <svg class="contact-icon" viewBox="0 0 12 12" fill="none" stroke="#c8c8cb" stroke-width="1.3"><rect x="1" y="2.5" width="10" height="7"/><path d="M1 2.5 L6 6.5 L11 2.5"/></svg>
          Darrel@Plankhorn.com
        </li>
        <li class="contact-item">
          <svg class="contact-icon" viewBox="0 0 12 12" fill="none" stroke="#c8c8cb" stroke-width="1.2"><circle cx="6" cy="6" r="5"/><ellipse cx="6" cy="6" rx="2.2" ry="5"/><path d="M1 6 H11"/></svg>
          www.Plankhorn.com
        </li>
      </ul>
      <p class="address">2817 Larchmont Avenue Dayton, OH 45409</p>
    </section>
  </main>
</body>
</html>
```